Slider needed for Database Documentation Topic

We need a slider to promote a content area of a web site. I'm listing this as a poster because the posters I have seen on FrameHarbor portfolios most closely resemble the combination or art and text I am looking for.
The content area we are promoting with this graphic will clarify the design and use of a complicated database. The title of the content area is "The Kindled VQ Database" and the banner should use that title.
To 'illuminate' something means to cast light on it, and this content area will help shed light on a complicated thing – the content will use diagrams, text, and examples to clarify the database. Another meaning is that an illuminated manuscript is a manuscript brought to life with pictures, and in a way that is also what this content area will do.
One idea for the slider might be a light bulb, lamp, candle or flashlight lighting up the words "VQ Database". Another idea would be the type of illustration you see if you search for "Illuminated manuscript"
But I'm not committed to any particular idea - in the past I have been pleased to see ideas that are different than my own but accomplish the same thing, so please feel free to use your judgement or ask any questions.
In addition to the title (The Kindled VQ Database) the graphic should allow room for three smaller lines of text – the three bullet items below:
- Guide to understanding the VQ database
- Data sources, uses and relationships explained with illustrations
- New content! Customers
The last bullet item will change as the content is added.
Some particulars ...
SIZE - 600 high x 1200 wide pixels
PHOTOS vs ILLUSTRATION - I am open to either one.

```html
<!DOCTYPE html>
<html lang="en">
<head>
<meta charset="utf-8">
<title>The Kindled VQ Database</title>
<link rel="stylesheet" href="https://fonts.googleapis.com/css2?family=Open+Sans:wght@300;400;700;800&family=Roboto+Condensed:wght@400&display=swap">
<style>
  :root {
    --deep-blue: #0a2a9e;
    --royal-blue: #1248d6;
    --bright-blue: #2a7bf0;
    --glow-cyan: #9fe8ff;
    --title-white: #ffffff;
    --title-lime: #b8ec2a;
    --bullet-white: #f2f7ff;
  }
  html, body {
    margin: 0;
    padding: 0;
    width: 1200px;
    height: 600px;
    overflow: hidden;
    background: var(--deep-blue);
  }
  .slider {
    position: relative;
    width: 1200px;
    height: 600px;
    overflow: hidden;
    background:
      radial-gradient(ellipse 420px 300px at 1010px 230px, rgba(159,232,255,0.75), rgba(42,123,240,0) 70%),
      radial-gradient(ellipse 900px 160px at 760px 120px, rgba(120,200,255,0.35), rgba(42,123,240,0) 70%),
      radial-gradient(ellipse 1100px 140px at 600px 560px, rgba(90,170,255,0.45), rgba(42,123,240,0) 70%),
      linear-gradient(160deg, var(--royal-blue) 0%, var(--deep-blue) 45%, var(--royal-blue) 75%, var(--bright-blue) 100%);
    font-family: "Open Sans", Arial, sans-serif;
  }
  .light-swoosh {
    position: absolute;
    inset: 0;
  }
  .bulb-art {
    position: absolute;
    left: 920px;
    top: 92px;
    width: 210px;
    height: 440px;
    border-radius: 105px 105px 40px 40px;
    background: radial-gradient(ellipse 60% 45% at 50% 38%, rgba(220,248,255,0.85), rgba(120,200,255,0.45) 60%, rgba(42,123,240,0) 100%);
  }
  .title {
    position: absolute;
    left: 46px;
    top: 130px;
    margin: 0;
    color: var(--title-white);
    line-height: 1;
    text-transform: uppercase;
    text-shadow: 0 2px 8px rgba(0, 20, 90, 0.35);
  }
  .title-line {
    display: block;
    white-space: nowrap;
  }
  .title-line--top {
    font-size: 104px;
    letter-spacing: -1px;
  }
  .title-article {
    font-weight: 300;
  }
  .title-highlight {
    font-weight: 800;
    color: var(--title-lime);
  }
  .title-line--main {
    margin-top: 4px;
    font-size: 116px;
    font-weight: 700;
    letter-spacing: -1px;
  }
  .features {
    position: absolute;
    left: 52px;
    top: 368px;
    margin: 0;
    padding: 0;
    list-style: none;
    font-family: "Roboto Condensed", "Arial Narrow", sans-serif;
    font-size: 29px;
    line-height: 43px;
    color: var(--bullet-white);
  }
  .features li::before {
    content: "\2022";
    margin-right: 8px;
  }
</style>
</head>
<body>
  <main class="slider">
    <svg class="light-swoosh" width="1200" height="600" viewBox="0 0 1200 600" aria-hidden="true">
      <path d="M0 40 C300 0 700 120 1200 60" fill="none" stroke="rgba(170,225,255,0.25)" stroke-width="3"/>
      <path d="M200 600 C500 470 900 470 1200 380" fill="none" stroke="rgba(170,225,255,0.35)" stroke-width="4"/>
      <path d="M0 560 C400 520 800 560 1200 470" fill="none" stroke="rgba(170,225,255,0.25)" stroke-width="3"/>
      <path d="M500 0 C700 120 950 180 1200 170" fill="none" stroke="rgba(200,240,255,0.3)" stroke-width="2"/>
    </svg>
    <div class="bulb-art" role="img" aria-label="Glowing glass light bulb with visible filament and screw base"></div>
    <h1 class="title">
      <span class="title-line title-line--top"><span class="title-article">The </span><span class="title-highlight">Kindled</span></span>
      <span class="title-line title-line--main">VQ Database</span>
    </h1>
    <ul class="features">
      <li>Guide to understanding the VQ database</li>
      <li>Data sources, uses and relationships explained with illustrations</li>
      <li>New content! Customers</li>
    </ul>
  </main>
</body>
</html>
```